Pull Up Banner Design for finance broker

We are requiring a design for pull up banners. KTV Finance provides finance services for a range of business equipment purchases including trucks, excavators, vehicle hoists and other industrial equipment. We are looking for a generic design that is not industry specific that we can place in dealerships that refer their clients to us to obtain their finance. The image we have selected (Attached) should be faint in the back ground (Or if you have alternative ideas/layout/image)

Size 2000mm x 800mm

Target Market(s)

Businesses requiring finance for equipment purchases

Industry/Entity Type

Finance

Requirements
Must have
• Banner to include the following text:
• Key Text:
• "Equipment Finance"
• "25+ Lenders" (Feature)
• Information Text:
• "Start-up / Existing Businesses"
• "New / Used"
• "Fast Approvals"
• "Flexible Options"
• Company/contact Text:
• "A dedicated team working for you" (Slogan)
• "1300 864 592"
• "www.ktvfinance.example.au"
• Logo: Attached - colours can be reversed (Banner colours to be used from this
Nice to have
• preference is darker background - not white

```html
<!DOCTYPE html>
<html lang="en">
<head>
<meta charset="utf-8">
<title>KTV Finance – Equipment Finance Pull Up Banner</title>
<link rel="stylesheet" href="https://fonts.googleapis.com/css2?family=Poppins:wght@500;600;700&family=Open+Sans:ital,wght@1,400&display=swap">
<style>
  :root {
    --orange: #e8631f;
    --ink: #1f1f24;
    --panel-dark: #16171c;
    --panel-mid: #262830;
    --white: #ffffff;
    --slogan-grey: #3a3a3a;
    --photo-light: #c9d0d6;
    --photo-mid: #6f7884;
    --photo-dark: #2c3440;
  }
  html, body {
    margin: 0;
    padding: 0;
    width: 1200px;
    height: 2909px;
    overflow: hidden;
    background: var(--white);
  }
  .banner {
    position: relative;
    width: 1200px;
    height: 2909px;
    background: var(--white);
    font-family: "Poppins", sans-serif;
  }
  .brand {
    position: absolute;
    top: 150px;
    left: 0;
    width: 1200px;
    display: flex;
    justify-content: center;
    align-items: center;
    gap: 26px;
  }
  .brand-mark {
    width: 100px;
    height: 100px;
    background: var(--orange);
  }
  .brand-name {
    font-family: "Poppins", sans-serif;
    font-weight: 700;
    font-size: 62px;
    letter-spacing: 3px;
    color: var(--ink);
    line-height: 1;
  }
  .panel-art {
    position: absolute;
    top: 0;
    left: 0;
  }
  .headline {
    position: absolute;
    left: 148px;
    top: 1400px;
    margin: 0;
    font-family: "Poppins", sans-serif;
    font-weight: 700;
    font-size: 134px;
    line-height: 151px;
    letter-spacing: 1px;
    color: var(--white);
  }
  .lenders {
    position: absolute;
    left: 156px;
    top: 1722px;
    margin: 0;
    font-weight: 500;
    font-size: 90px;
    line-height: 1;
    color: var(--white);
  }
  .lenders .count { color: var(--orange); }
  .features {
    position: absolute;
    left: 150px;
    top: 1905px;
    margin: 0;
    padding: 0;
    list-style: none;
    font-weight: 500;
    font-size: 57px;
    line-height: 78px;
    color: var(--white);
  }
  .features li {
    position: relative;
    padding-left: 76px;
    margin-bottom: 32px;
  }
  .features li::before {
    content: "";
    position: absolute;
    left: 0;
    top: 24px;
    width: 32px;
    height: 32px;
    background: var(--orange);
    border-radius: 4px;
  }
  .contact {
    position: absolute;
    left: 150px;
    top: 2500px;
  }
  .phone {
    display: flex;
    align-items: center;
    gap: 26px;
    font-weight: 500;
    font-size: 72px;
    line-height: 1;
    color: var(--white);
  }
  .phone-icon { width: 62px; height: 62px; }
  .web {
    margin-top: 30px;
    font-weight: 500;
    font-size: 56px;
    line-height: 1;
    color: var(--orange);
  }
  .slogan {
    position: absolute;
    left: 0;
    top: 2745px;
    width: 1200px;
    margin: 0;
    text-align: center;
    font-family: "Open Sans", sans-serif;
    font-style: italic;
    font-weight: 400;
    font-size: 58px;
    color: var(--slogan-grey);
  }
</style>
</head>
<body>
<div class="banner">
  <div class="brand">
    <div class="brand-mark"></div>
    <div class="brand-name">KTV FINANCE</div>
  </div>

  <svg class="panel-art" width="1200" height="2909" viewBox="0 0 1200 2909">
    <defs>
      <linearGradient id="panelShade" x1="0" y1="0" x2="1" y2="1">
        <stop offset="0" stop-color="var(--panel-mid)"/>
        <stop offset="1" stop-color="var(--panel-dark)"/>
      </linearGradient>
      <linearGradient id="photoTone" x1="0" y1="0" x2="1" y2="1">
        <stop offset="0" stop-color="var(--photo-light)"/>
        <stop offset="0.55" stop-color="var(--photo-mid)"/>
        <stop offset="1" stop-color="var(--photo-dark)"/>
      </linearGradient>
      <clipPath id="panelClip">
        <rect x="29" y="333" width="1144" height="2393"/>
      </clipPath>
    </defs>
    <rect class="dark-panel" x="29" y="333" width="1144" height="2393" fill="url(#panelShade)"/>
    <polygon class="hero-photo" role="img" aria-label="Photo of two businessmen in suits reviewing documents and a tablet at an office desk"
      points="29,333 1173,333 1173,986 596,1229 29,1100" fill="url(#photoTone)"/>
    <polygon class="chevron-band" points="29,1100 596,1229 1173,986 1173,1071 596,1334 29,1156" fill="var(--orange)"/>
    <g clip-path="url(#panelClip)">
      <polyline class="corner-chevron" points="1200,2360 1040,2510 1200,2660" fill="none" stroke="var(--orange)" stroke-width="44" stroke-linejoin="round"/>
    </g>
  </svg>

  <h1 class="headline">EQUIPMENT<br>FINANCE</h1>
  <p class="lenders"><span class="count">25+</span> Lenders</p>

  <ul class="features">
    <li>Start-up / Existing<br>Businesses</li>
    <li>New / Used</li>
    <li>Fast Approvals</li>
    <li>Flexible Options</li>
  </ul>

  <div class="contact">
    <div class="phone">
      <svg class="phone-icon" viewBox="0 0 66 66" aria-hidden="true">
        <rect width="66" height="66" rx="10" fill="var(--orange)"/>
        <path d="M20 15c2-1 4 0 5 2l4 7c1 2 0 4-1 5l-3 2c2 5 6 9 11 11l2-3c1-1 3-2 5-1l7 4c2 1 3 3 2 5l-2 4c-1 2-4 3-7 2C29 49 17 37 13 23c-1-3 0-6 2-7z" fill="var(--white)"/>
      </svg>
      <span>1300 864 592</span>
    </div>
    <div class="web">www.ktvfinance.example.au</div>
  </div>

  <p class="slogan">A dedicated team working for you</p>
</div>
</body>
</html>
```